Illustrationen für Termin-Tool
Zielgruppe
Buchwelle.de ist ein Termin-Tool. Unternehmen mit Ladengeschäft können darüber eigene Terminformulare erstellen und diese auf ihrer Website einbinden. Kunden können dann einen Termin buchen.
Zielgruppe: Dienstleister wie Friseure, Fotografen, Beauty-Salons, Werkstätten. Also alle Ladengeschäfte, die Termine bisher meist telefonisch vereinbart haben.
Aufgabenstellung
Unsere Kunden können drei verschiedene Voreinstellungen für die Terminerinnerungen auswählen.
Derzeitige Arbeitstitel für diese drei Voreinstellungen: SELTEN, MODERAT, HÄUFIG (siehe Screenshot anbei oder auf Buchwelle.de nach der Registrierung im Kunden-Bereich unter TERMINERINNERUNGEN BEARBEITEN.
Diese drei Voreinstellungen sollen grafisch dargestellt werden in Form von drei Tieren (Elefant, Eichhörnchen, Flamingo) + Text (siehe nachfolgend). Diese sollen sich harmonisch in das Corporate-Design von Buchwelle einfügen.
Voreinstellung Terminerinnerung SELTEN:
Für Kunden mit einem Elefanten-Gedächtnis + Comic-Elefant
Voreinstellung Terminerinnerung MODERAT:
'Wo hab´ ich die Nüsse denn bloß vergraben?' + Comic-Eichhörnchen
Voreinstellung Terminerinnerung HÄUFIG:
Für Kunden mit einem Flamingo-Kurzzeitgedächtnis. + Comic-Flamingo
Vom Look&Feel bitte die aktuellen Comic-Figuren vorab betrachten auf Buchwelle.de: Branchenfiguren (unten auf der Seite) + WELLO (siehe Banner oben auf der Seite)
Die drei Banner können bitte mit Text und jeweiliger Comic-Figur erstellt werden. Banner-Größe (SELTEN, MODERAT, HÄUFIG) siehe bitte Datei anbei: designenlassen01_1.jpg
Falls der Platz ausreicht, können die Banner zusätzlich die Begrifflichkeiten enthalten: SELTEN, MODERAT, HÄUFIG
Beispiel, Siehe anbei: designenlassen01_1_.jpg
Hier können Sie bitte kreativ die beste Lösung finden für die drei Banner. Der Kunde soll später die Verbindung erkennen können:
Elefanten-Voreinstellung = für nicht vergessliche Kunden
Eichhörnchen-Voreinstellung = für mittelmäßig vergessliche Kunden
Flamingo-Voreinstellung = für sehr vergessliche Kunden
Die Figuren sollen gerne einen passenden Ausruck/Typ zeigen (nur Ideen, können auch abgewandelt werden):
Elefant = abgeklärter, cooler, schlauer Elefant, der nichts vergisst
Eichhörnchen = etwas überdreht, jugendlicher Hall..

```html
<!DOCTYPE html>
<html lang="de">
<head>
<meta charset="utf-8">
<title>Terminerinnerungen – Voreinstellungen</title>
<link href="https://fonts.googleapis.com/css2?family=Montserrat:wght@300;400;600&family=Roboto:wght@500;700&display=swap" rel="stylesheet">
<style>
:root{
  --bg:#ffffff;
  --grey-band:#c4c6c5;
  --teal:#73c2b8;
  --teal-light:#e9f6f4;
  --pill:#6c757d;
  --text:#555a5e;
  --text-light:#6b7075;
  --line:#e3e5e6;
  --ink:#2b2b2b;
  --eine:#a7a9ab;
  --drei:#c47536;
  --fuenf:#e35aa1;
}
*{box-sizing:border-box;margin:0;padding:0}
html,body{width:833px;height:1200px;overflow:hidden;background:var(--bg)}
body{position:relative;font-family:"Montserrat",sans-serif;color:var(--text)}
.row{position:absolute;left:0;width:833px;overflow:hidden}
.row-grey{top:8px;height:325px}
.row-teal{top:340px;height:373px}
.row-fade{top:721px;height:479px}
.card{position:absolute;top:0;width:248px;background:#fff;box-shadow:0 1px 4px rgba(0,0,0,.12);padding-bottom:12px}
.banner{position:relative;height:141px;overflow:hidden}
.row-grey .banner{background:var(--grey-band)}
.row-teal .banner{background:var(--teal)}
.row-fade .banner{background:linear-gradient(180deg,var(--teal) 0%,var(--teal-light) 100%)}
.banner-panel{position:absolute;left:16px;top:16px;width:215px;height:110px;background:#fff}
.row-fade .banner-panel{background:transparent}
.banner-text{position:absolute;left:27px;top:24px;width:150px;font-family:"Roboto",sans-serif;color:var(--ink)}
.banner-title{font-size:11.5px;font-weight:500;line-height:12.5px}
.banner-title .count{font-size:15.5px;font-weight:500}
.eine{color:var(--eine)} .drei{color:var(--drei)} .fuenf{color:var(--fuenf)}
.banner-sub{position:absolute;left:0;top:76px;width:170px;font-size:8.2px;font-weight:700;line-height:12.5px}
.figure{position:absolute;right:2px;top:4px;width:96px;height:137px;border-radius:44px 44px 10px 10px}
.fig-elephant{background:linear-gradient(180deg,#b9bbbd,#9ea0a2)}
.fig-squirrel{background:linear-gradient(180deg,#c98a4f,#a9683a)}
.fig-flamingo{background:linear-gradient(180deg,#ee8fbf,#d8619f)}
.body{padding:0 11px 0 13px}
.pill{margin-top:9px;height:12px;border-radius:6px;background:var(--pill);color:#fff;font-size:8px;font-weight:600;line-height:12px;text-align:center}
.pill svg{width:7px;height:7px;vertical-align:-1px;margin-right:1px}
.divider{height:1px;background:var(--line);margin-top:13px}
.section-head{margin-top:10px;font-size:9.8px;font-weight:600;line-height:11px;color:var(--text)}
.section-head svg{width:9px;height:8px;vertical-align:-1px;margin-right:1px}
.list{margin-top:4px;border:1px solid var(--line)}
.list li{list-style:none;height:23px;line-height:22px;padding-left:9px;font-size:10px;font-weight:300;color:var(--text-light);border-top:1px solid var(--line)}
.list li:first-child{border-top:0}
.list svg{width:8px;height:8px;vertical-align:-1px;margin-right:2px}
.select{margin-top:11px;height:21px;border:1px solid #8f9396;border-radius:2px;padding:0 9px;font-size:10px;font-weight:300;line-height:19px;color:var(--text-light);position:relative}
.select::after{content:"";position:absolute;right:6px;top:8px;border:3px solid transparent;border-top:4px solid #333}
.button{margin-top:11px;height:21px;background:var(--teal);color:#fff;font-size:10px;font-weight:400;line-height:21px;text-align:center}
.note{margin-top:8px;font-size:8px;font-weight:300;color:var(--text-light)}
.note svg{width:8px;height:7px;vertical-align:-1px}
.gap{margin-top:13px}
</style>
</head>
<body>
<svg width="0" height="0" style="position:absolute">
  <defs>
    <symbol id="i-tick" viewBox="0 0 10 10"><path d="M1 5.5 4 8.5 9 1.5" fill="none" stroke="#fff" stroke-width="2"/></symbol>
    <symbol id="i-mail" viewBox="0 0 10 8"><rect x="0.5" y="0.5" width="9" height="7" fill="#7a7f84"/><path d="M0.5 0.5 5 4.5 9.5 0.5M0.5 7.5 4 4M9.5 7.5 6 4" fill="none" stroke="#fff" stroke-width="0.8"/></symbol>
    <symbol id="i-bell" viewBox="0 0 10 10"><path d="M5 0.8c-2 0-3 1.6-3 3.6v2.3L1 8h8L8 6.7V4.4C8 2.4 7 .8 5 .8z" fill="#6c7176"/><circle cx="5" cy="9" r="1" fill="#6c7176"/></symbol>
    <symbol id="i-phone" viewBox="0 0 8 10"><rect x="1" y="0.6" width="6" height="8.8" rx="1" fill="none" stroke="#555a5e" stroke-width="1.1"/></symbol>
    <symbol id="i-warn" viewBox="0 0 10 9"><path d="M5 .7 9.5 8.5H.5z" fill="none" stroke="#555a5e"/><path d="M5 3.5v2.5M5 7v.6" stroke="#555a5e"/></symbol>
  </defs>
</svg>

<!-- ===== Row: grey band ===== -->
<section class="row row-grey">
  <article class="card" style="left:21px">
    <header class="banner"><div class="banner-panel"></div>
      <div class="banner-text"><p class="banner-title"><span class="count eine">Eine</span> automatische<br>Terminerinnerung<br>per Email</p><p class="banner-sub">Für Kunden mit<br>Elefanten-Langzeitgedächtnis</p></div>
      <div class="figure fig-elephant" role="img" aria-label="Comic-Elefant, winkend"></div></header>
    <div class="body">
      <p class="pill"><svg><use href="#i-tick"/></svg>1 Termin-Erinnerungen</p><div class="divider"></div>
      <p class="section-head"><svg><use href="#i-mail"/></svg>1 Termin-Erinnerungen<br>per E-Mail</p>
      <ul class="list"><li><svg><use href="#i-bell"/></svg>3 Tage vor Termin</li></ul>
      <div class="select">-- Terminformular --</div><div class="button">jetzt übernehmen</div>
    </div>
  </article>
  <article class="card" style="left:286px">
    <header class="banner"><div class="banner-panel"></div>
      <div class="banner-text"><p class="banner-title"><span class="count drei">Drei</span> automatische<br>Terminerinnerungen<br>per Email</p><p class="banner-sub">Für vergessliche Kunden<br>und hohle Nüsse</p></div>
      <div class="figure fig-squirrel" role="img" aria-label="Comic-Eichhörnchen mit Nuss"></div></header>
    <div class="body">
      <p class="pill"><svg><use href="#i-tick"/></svg>4 Termin-Erinnerungen</p><div class="divider"></div>
      <p class="section-head"><svg><use href="#i-mail"/></svg>2 Termin-Erinnerungen<br>per E-Mail</p>
      <ul class="list"><li><svg><use href="#i-bell"/></svg>7 Tage vor Termin</li><li><svg><use href="#i-bell"/></svg>1 Tag vor Termin</li></ul>
      <div class="divider gap"></div>
      <p class="section-head"><svg><use href="#i-phone"/></svg>2 Termin-Erinnerungen<br>per SMS</p>
      <ul class="list"><li><svg><use href="#i-bell"/></svg>4 Tage vor Termin</li><li><svg><use href="#i-bell"/></svg>2 Tage vor Termin</li></ul>
    </div>
  </article>
  <article class="card" style="left:548px">
    <header class="banner"><div class="banner-panel"></div>
      <div class="banner-text"><p class="banner-title"><span class="count fuenf">Fünf</span> automatische<br>Terminerinnerungen<br>per Email</p><p class="banner-sub">Für Kunden mit<br>Flamingo-Kurzzeitgedächtnis.</p></div>
      <div class="figure fig-flamingo" role="img" aria-label="Comic-Flamingo"></div></header>
    <div class="body">
      <p class="pill"><svg><use href="#i-tick"/></svg>6 Termin-Erinnerungen</p><div class="divider"></div>
      <p class="section-head"><svg><use href="#i-mail"/></svg>3 Termin-Erinnerungen<br>per E-Mail</p>
      <ul class="list"><li><svg><use href="#i-bell"/></svg>14 Tage vor Termin</li><li><svg><use href="#i-bell"/></svg>7 Tage vor Termin</li><li><svg><use href="#i-bell"/></svg>1 Tag vor Termin</li></ul>
      <div class="divider gap"></div>
      <p class="section-head"><svg><use href="#i-phone"/></svg>3 Termin-Erinnerungen<br>per SMS</p>
    </div>
  </article>
</section>

<!-- ===== Row: teal band ===== -->
<section class="row row-teal">
  <article class="card" style="left:16px">
    <header class="banner"><div class="banner-panel"></div>
      <div class="banner-text"><p class="banner-title"><span class="count eine">Eine</span> automatische<br>Terminerinnerung<br>per Email</p><p class="banner-sub">Für Kunden mit<br>Elefanten-Langzeitgedächtnis</p></div>
      <div class="figure fig-elephant" role="img" aria-label="Comic-Elefant, winkend"></div></header>
    <div class="body">
      <p class="pill"><svg><use href="#i-tick"/></svg>1 Termin-Erinnerungen</p><div class="divider"></div>
      <p class="section-head"><svg><use href="#i-mail"/></svg>1 Termin-Erinnerungen<br>per E-Mail</p>
      <ul class="list"><li><svg><use href="#i-bell"/></svg>3 Tage vor Termin</li></ul>
      <div class="select">-- Terminformular --</div><div class="button">jetzt übernehmen</div>
    </div>
  </article>
  <article class="card" style="left:281px">
    <header class="banner"><div class="banner-panel"></div>
      <div class="banner-text"><p class="banner-title"><span class="count drei">Drei</span> automatische<br>Terminerinnerungen<br>per Email</p><p class="banner-sub">Für vergessliche Kunden<br>und hohle Nüsse</p></div>
      <div class="figure fig-squirrel" role="img" aria-label="Comic-Eichhörnchen mit Nuss"></div></header>
    <div class="body">
      <p class="pill"><svg><use href="#i-tick"/></svg>4 Termin-Erinnerungen</p><div class="divider"></div>
      <p class="section-head"><svg><use href="#i-mail"/></svg>2 Termin-Erinnerungen<br>per E-Mail</p>
      <ul class="list"><li><svg><use href="#i-bell"/></svg>7 Tage vor Termin</li><li><svg><use href="#i-bell"/></svg>1 Tag vor Termin</li></ul>
      <div class="divider gap"></div>
      <p class="section-head"><svg><use href="#i-phone"/></svg>2 Termin-Erinnerungen<br>per SMS</p>
      <ul class="list"><li><svg><use href="#i-bell"/></svg>4 Tage vor Termin</li><li><svg><use href="#i-bell"/></svg>2 Tage vor Termin</li></ul>
    </div>
  </article>
  <article class="card" style="left:543px">
    <header class="banner"><div class="banner-panel"></div>
      <div class="banner-text"><p class="banner-title"><span class="count fuenf">Fünf</span> automatische<br>Terminerinnerungen<br>per Email</p><p class="banner-sub">Für Kunden mit<br>Flamingo-Kurzzeitgedächtnis.</p></div>
      <div class="figure fig-flamingo" role="img" aria-label="Comic-Flamingo"></div></header>
    <div class="body">
      <p class="pill"><svg><use href="#i-tick"/></svg>6 Termin-Erinnerungen</p><div class="divider"></div>
      <p class="section-head"><svg><use href="#i-mail"/></svg>3 Termin-Erinnerungen<br>per E-Mail</p>
      <ul class="list"><li><svg><use href="#i-bell"/></svg>14 Tage vor Termin</li><li><svg><use href="#i-bell"/></svg>7 Tage vor Termin</li><li><svg><use href="#i-bell"/></svg>1 Tag vor Termin</li></ul>
      <div class="divider gap"></div>
      <p class="section-head"><svg><use href="#i-phone"/></svg>3 Termin-Erinnerungen<br>per SMS</p>
      <ul class="list"><li><svg><use href="#i-bell"/></svg>12 Tage vor Termin</li><li><svg><use href="#i-bell"/></svg>4 Tage vor Termin</li></ul>
    </div>
  </article>
</section>

<!-- ===== Row: gradient band ===== -->
<section class="row row-fade">
  <article class="card" style="left:14px">
    <header class="banner"><div class="banner-panel"></div>
      <div class="banner-text"><p class="banner-title"><span class="count eine">Eine</span> automatische<br>Terminerinnerung<br>per Email</p><p class="banner-sub">Für Kunden mit<br>Elefanten-Langzeitgedächtnis</p></div>
      <div class="figure fig-elephant" role="img" aria-label="Comic-Elefant, winkend"></div></header>
    <div class="body">
      <p class="pill"><svg><use href="#i-tick"/></svg>1 Termin-Erinnerungen</p><div class="divider"></div>
      <p class="section-head"><svg><use href="#i-mail"/></svg>1 Termin-Erinnerungen<br>per E-Mail</p>
      <ul class="list"><li><svg><use href="#i-bell"/></svg>3 Tage vor Termin</li></ul>
      <div class="select">-- Terminformular --</div><div class="button">jetzt übernehmen</div>
    </div>
  </article>
  <article class="card" style="left:278px">
    <header class="banner"><div class="banner-panel"></div>
      <div class="banner-text"><p class="banner-title"><span class="count drei">Drei</span> automatische<br>Terminerinnerungen<br>per Email</p><p class="banner-sub">Für vergessliche Kunden<br>und hohle Nüsse</p></div>
      <div class="figure fig-squirrel" role="img" aria-label="Comic-Eichhörnchen mit Nuss"></div></header>
    <div class="body">
      <p class="pill"><svg><use href="#i-tick"/></svg>4 Termin-Erinnerungen</p><div class="divider"></div>
      <p class="section-head"><svg><use href="#i-mail"/></svg>2 Termin-Erinnerungen<br>per E-Mail</p>
      <ul class="list"><li><svg><use href="#i-bell"/></svg>7 Tage vor Termin</li><li><svg><use href="#i-bell"/></svg>1 Tag vor Termin</li></ul>
      <div class="divider gap"></div>
      <p class="section-head"><svg><use href="#i-phone"/></svg>2 Termin-Erinnerungen<br>per SMS</p>
      <ul class="list"><li><svg><use href="#i-bell"/></svg>4 Tage vor Termin</li><li><svg><use href="#i-bell"/></svg>2 Tage vor Termin</li></ul>
      <div class="select">-- Terminformular --</div><div class="button">jetzt übernehmen</div>
      <p class="note"><svg><use href="#i-warn"/></svg>SMS-Freischaltung wird benötigt.</p>
    </div>
  </article>
  <article class="card" style="left:541px">
    <header class="banner"><div class="banner-panel"></div>
      <div class="banner-text"><p class="banner-title"><span class="count fuenf">Fünf</span> automatische<br>Terminerinnerungen<br>per Email</p><p class="banner-sub">Für Kunden mit<br>Flamingo-Kurzzeitgedächtnis.</p></div>
      <div class="figure fig-flamingo" role="img" aria-label="Comic-Flamingo"></div></header>
    <div class="body">
      <p class="pill"><svg><use href="#i-tick"/></svg>6 Termin-Erinnerungen</p><div class="divider"></div>
      <p class="section-head"><svg><use href="#i-mail"/></svg>3 Termin-Erinnerungen<br>per E-Mail</p>
      <ul class="list"><li><svg><use href="#i-bell"/></svg>14 Tage vor Termin</li><li><svg><use href="#i-bell"/></svg>7 Tage vor Termin</li><li><svg><use href="#i-bell"/></svg>1 Tag vor Termin</li></ul>
      <div class="divider gap"></div>
      <p class="section-head"><svg><use href="#i-phone"/></svg>3 Termin-Erinnerungen<br>per SMS</p>
      <ul class="list"><li><svg><use href="#i-bell"/></svg>12 Tage vor Termin</li><li><svg><use href="#i-bell"/></svg>4 Tage vor Termin</li><li><svg><use href="#i-bell"/></svg>2 Tage vor Termin</li></ul>
      <div class="select">-- Terminformular --</div><div class="button">jetzt übernehmen</div>
      <p class="note"><svg><use href="#i-warn"/></svg>SMS-Freischaltung wird benötigt.</p>
    </div>
  </article>
</section>
</body>
</html>
```